Bref créative
Business Cards & Satationary for Copperfield Homes
Dallin Marsh
Professional
Copperfield Homes
PO Box 587
KELMORE RISE Q 4390
M: 0417 562 908
info@copperfieldhomes.com.au
www.copperfieldhomes.com.au
NHRA Licence No. 80394. Housing Registry Office of Tasmania No. HR-K61402
Residential Construction
"Builder of Quality not Quantity"
E:info@copperfieldhomes.com.au

```html
<!DOCTYPE html>
<html lang="en">
<head>
<meta charset="utf-8">
<title>Copperfield Homes – Business Card</title>
<link rel="stylesheet" href="https://fonts.googleapis.com/css2?family=Open+Sans:wght@400;600&display=swap">
<style>
  :root {
    --backdrop: #e9e6e2;
    --card-white: #ffffff;
    --card-fade: #e6e6e6;
    --header-dark: #1f2a33;
    --header-mid: #3b4a56;
    --copper: #d4461b;
    --copper-light: #e8622c;
    --steel: #9a9a9a;
    --ink: #3a3a3a;
    --ink-soft: #555555;
  }
  * { box-sizing: border-box; margin: 0; padding: 0; }
  html, body { width: 1200px; height: 896px; overflow: hidden; }
  body {
    background: var(--backdrop);
    font-family: "Open Sans", Arial, sans-serif;
    position: relative;
  }
  .card {
    position: absolute;
    width: 564px;
    height: 300px;
    background: var(--card-white);
    box-shadow: 0 6px 18px rgba(0,0,0,0.25);
    overflow: hidden;
  }
  /* Front: contact side */
  .card-front { left: 73px; top: 73px; }
  .card-front .header {
    position: absolute; left: 0; top: 0; width: 100%; height: 150px;
    background: linear-gradient(90deg, var(--header-dark) 0%, var(--header-mid) 50%, var(--header-dark) 100%);
    border-bottom: 3px solid #c9cdd0;
    display: flex; align-items: center; justify-content: center;
  }
  .brand { display: flex; align-items: center; gap: 12px; }
  .brand-square { width: 34px; height: 34px; background: var(--copper); }
  .brand-name {
    font-weight: 600; font-size: 28px; letter-spacing: 1px;
    text-transform: uppercase;
  }
  .card-front .brand-name { color: #ffffff; }
  .card-front .body {
    position: absolute; left: 0; top: 153px; width: 100%; height: 147px;
    background: linear-gradient(180deg, #ffffff 0%, #f1f1f1 100%);
  }
  .holder-name {
    position: absolute; left: 22px; top: 40px;
    color: var(--copper); font-weight: 600; font-size: 15px;
  }
  .contact-list {
    position: absolute; left: 330px; top: 36px; list-style: none;
  }
  .contact-list li {
    display: flex; align-items: center; gap: 7px;
    font-size: 12px; color: var(--ink-soft); line-height: 19px;
  }
  .contact-list svg { width: 12px; height: 12px; flex: none; }
  /* Back: logo side */
  .card-back {
    left: 605px; top: 510px;
    background: linear-gradient(180deg, #ffffff 0%, var(--card-fade) 100%);
  }
  .card-back .brand {
    position: absolute; left: 0; top: 0; width: 100%; height: 230px;
    justify-content: center;
  }
  .card-back .brand-name { color: var(--ink); }
  .card-back .band { position: absolute; left: 0; bottom: 22px; width: 100%; height: 22px; }
</style>
</head>
<body>

<section class="card card-front" aria-label="Business card, contact side">
  <div class="header">
    <div class="brand">
      <span class="brand-square"></span>
      <span class="brand-name">Copperfield Homes</span>
    </div>
  </div>
  <div class="body">
    <p class="holder-name">Dallin Marsh</p>
    <ul class="contact-list">
      <li>
        <svg viewBox="0 0 12 12"><circle cx="6" cy="6" r="6" fill="var(--copper)"/><path d="M6 2.6a2.2 2.2 0 0 0-2.2 2.2C3.8 6.6 6 9.4 6 9.4s2.2-2.8 2.2-4.6A2.2 2.2 0 0 0 6 2.6z" fill="#fff"/></svg>
        587 Kelmore Rise Q 4390
      </li>
      <li>
        <svg viewBox="0 0 12 12"><circle cx="6" cy="6" r="6" fill="var(--copper)"/><path d="M4 3l1.2 1.4-.6.8c.4.9 1.1 1.6 2 2l.8-.6L9 7.8 8.3 9C6 9 3 6 3 3.7z" fill="#fff"/></svg>
        0417 562 908
      </li>
      <li>
        <svg viewBox="0 0 12 12"><circle cx="6" cy="6" r="6" fill="var(--copper)"/><rect x="3" y="4" width="6" height="4.2" fill="#fff"/><path d="M3 4l3 2.3L9 4" stroke="var(--copper)" stroke-width="0.7" fill="none"/></svg>
        info@copperfieldhomes.com.au
      </li>
      <li>
        <svg viewBox="0 0 12 12"><circle cx="6" cy="6" r="6" fill="var(--copper)"/><circle cx="6" cy="6" r="3" fill="none" stroke="#fff" stroke-width="0.8"/><path d="M3 6h6M6 3c-1.4 1.8-1.4 4.2 0 6M6 3c1.4 1.8 1.4 4.2 0 6" stroke="#fff" stroke-width="0.6" fill="none"/></svg>
        www.copperfieldhomes.com.au
      </li>
    </ul>
  </div>
</section>

<section class="card card-back" aria-label="Business card, brand side">
  <div class="brand">
    <span class="brand-square"></span>
    <span class="brand-name">Copperfield Homes</span>
  </div>
  <svg class="band" viewBox="0 0 564 22" preserveAspectRatio="none" aria-hidden="true">
    <polygon points="0,6 340,6 356,0 564,0 564,22 0,22" fill="var(--steel)"/>
    <polygon points="0,6 330,6 314,22 0,22" fill="var(--copper)"/>
  </svg>
</section>

</body>
</html>
```